New business card design needed for Trucking/Staffing company!

I am looking for a business card design. The business name is Harbor Lane Freightworks, LLC. This company is a staffing company for commercial drivers/truck drivers. Most of our customers are trucking/supply companies. Our colors are blue/black/white/grey. The info I have on my current business cards is
-Spot for a name
-2 lines for an address
-3 lines for Office, cell, and fax
-email
-website(currently on backside of card with logo but can go anywhere)
Updates

Project Deadline Extended
Reason: Open to more designs

Target Market(s)

Trucking companies, building supply companies

Industry/Entity Type

Business

Contact Information for Business Card

Edgy but professional

Font styles to use
Other font styles liked:
• Open to suggestions

Colors
0555a3
000000
ffffff
9d9d9d

Requirements
Must have
• Must have the logo incorporated

```html
<!DOCTYPE html>
<html lang="en">
<head>
<meta charset="utf-8">
<title>Harbor Lane Freightworks — Business Card</title>
<link rel="stylesheet" href="https://fonts.googleapis.com/css2?family=Open+Sans:wght@400;600;700&display=swap">
<style>
  :root {
    --blue: #2c3a96;
    --charcoal: #2f2d2e;
    --charcoal-light: #3a3839;
    --white: #ffffff;
    --grey: #9d9d9d;
    --page: #e6e6e6;
  }
  * { margin: 0; padding: 0; box-sizing: border-box; }
  html, body { width: 1200px; height: 900px; overflow: hidden; }
  body {
    background: var(--page);
    font-family: "Open Sans", Arial, sans-serif;
    display: flex; flex-direction: column; align-items: center; justify-content: center;
    gap: 36px;
  }
  .card {
    width: 700px; height: 400px; position: relative; overflow: hidden;
    box-shadow: 0 6px 18px rgba(0,0,0,.25);
  }

  /* Back side */
  .card-back { background: linear-gradient(160deg, var(--charcoal-light), var(--charcoal) 60%); }
  .card-back .band { position: absolute; inset: 0; }
  .card-back .brand {
    position: absolute; left: 150px; top: 135px; width: 420px;
    color: var(--white); font-weight: 700; font-size: 34px; line-height: 1.15;
    display: flex; align-items: center; gap: 16px;
  }
  .brand-mark { width: 18px; height: 18px; background: var(--blue); flex: none; }
  .card-back .web {
    position: absolute; right: 70px; bottom: 48px;
    color: var(--white); font-size: 17px; transform: rotate(-16deg); transform-origin: right bottom;
  }

  /* Front side */
  .card-front { background: var(--white); }
  .front-top { position: absolute; left: 0; top: 0; width: 100%; height: 24px; background: var(--charcoal); border-bottom: 3px solid var(--blue); }
  .front-logo {
    position: absolute; left: 0; top: 27px; width: 100%; height: 168px;
    display: flex; align-items: center; justify-content: center; gap: 14px;
  }
  .front-logo .name { color: var(--blue); font-weight: 700; font-size: 34px; }
  .front-info {
    position: absolute; left: 0; top: 195px; width: 100%; height: 165px;
    background: var(--charcoal); border-top: 3px solid var(--blue); border-bottom: 3px solid var(--blue);
    display: flex; align-items: center; padding: 0 40px;
  }
  .person { width: 300px; text-align: right; padding-right: 26px; position: relative; }
  .person-name { color: #4a5bc4; font-size: 20px; margin-bottom: 22px; }
  .address { color: var(--white); font-size: 14px; line-height: 1.35; }
  .pin { position: absolute; right: -8px; top: 50px; }
  .divider { width: 1px; height: 120px; background: var(--blue); margin: 0 26px 0 8px; }
  .contacts { list-style: none; color: var(--white); font-size: 14px; }
  .contacts li { display: flex; align-items: center; gap: 14px; height: 22px; }
  .contacts svg { width: 15px; height: 15px; flex: none; }
</style>
</head>
<body>

  <section class="card card-back" aria-label="Card back">
    <svg class="band" viewBox="0 0 700 400" preserveAspectRatio="none" aria-hidden="true">
      <polygon points="700,170 700,215 210,400 100,400" fill="var(--blue)"/>
    </svg>
    <div class="brand"><span class="brand-mark"></span>Harbor Lane Freightworks, LLC</div>
    <div class="web">www.harborlanefreight.com</div>
  </section>

  <section class="card card-front" aria-label="Card front">
    <div class="front-top"></div>
    <div class="front-logo">
      <span class="brand-mark"></span>
      <span class="name">Harbor Lane Freightworks, LLC</span>
    </div>
    <div class="front-info">
      <div class="person">
        <p class="person-name">Dana Whitfield</p>
        <p class="address">Your Office address<br>in Just Two Line</p>
        <svg class="pin" width="14" height="18" viewBox="0 0 14 18" aria-hidden="true">
          <path d="M7 0a7 7 0 0 0-7 7c0 5 7 11 7 11s7-6 7-11a7 7 0 0 0-7-7z" fill="var(--blue)"/>
          <circle cx="7" cy="7" r="2.5" fill="var(--charcoal)"/>
        </svg>
      </div>
      <div class="divider"></div>
      <ul class="contacts">
        <li><svg viewBox="0 0 16 16" aria-hidden="true"><rect x="2" y="1" width="12" height="14" rx="1" fill="var(--blue)"/><rect x="4" y="3" width="8" height="3" fill="var(--charcoal)"/></svg>+1 855.410.6620</li>
        <li><svg viewBox="0 0 16 16" aria-hidden="true"><circle cx="8" cy="8" r="7" fill="none" stroke="var(--blue)" stroke-width="1.6"/><path d="M5 4l2 2-1 1.2c.6 1.3 1.5 2.2 2.8 2.8L10 9l2 2-1.3 1.2C7.5 12 4 8.5 3.8 5.3z" fill="var(--blue)"/></svg>508.362.7781</li>
        <li><svg viewBox="0 0 16 16" aria-hidden="true"><rect x="4" y="1" width="8" height="5" fill="var(--blue)"/><rect x="1" y="6" width="14" height="7" rx="1" fill="var(--blue)"/><rect x="4" y="10" width="8" height="5" fill="var(--white)"/></svg>508.362.7790</li>
        <li><svg viewBox="0 0 16 16" aria-hidden="true"><rect x="1" y="3" width="14" height="10" fill="none" stroke="var(--blue)" stroke-width="1.6"/><path d="M1 3l7 6 7-6" fill="none" stroke="var(--blue)" stroke-width="1.6"/></svg>dana@harborlanefreight.com</li>
        <li><svg viewBox="0 0 16 16" aria-hidden="true"><circle cx="8" cy="8" r="7" fill="var(--blue)"/><path d="M1 8h14M8 1c3 3.5 3 10.5 0 14M8 1c-3 3.5-3 10.5 0 14" fill="none" stroke="var(--charcoal)" stroke-width="1"/></svg>www.harborlanefreight.com</li>
      </ul>
    </div>
  </section>

</body>
</html>
```